Mt Brindlewood Hotel

We need a business card with old world charm.
The design will need to promote dining and accommodation for local residents as a place to relax and for vacationing or week-end visitors seeking an experience of country hospitality.
The hotel was originally opened in 1909.

Target Market(s)

Adults and Families searching for dining and accommodation.

Industry/Entity Type

Business

Requirements
Nice to have
• Sketch or line drawing of Hotel

```html
<!DOCTYPE html>
<html lang="en">
<head>
<meta charset="utf-8">
<title>Mt Brindlewood Hotel — Business Card</title>
<link rel="stylesheet" href="https://fonts.googleapis.com/css2?family=Carlito:ital,wght@0,400;0,700;1,400&display=swap">
<style>
  :root {
    --burgundy: #8a0b0c;
    --gold: #f0a500;
    --cream: #fbf6ea;
    --white: #ffffff;
  }
  html, body {
    margin: 0;
    padding: 0;
    width: 1200px;
    height: 691px;
    overflow: hidden;
    background: var(--burgundy);
  }
  .card {
    position: relative;
    width: 1200px;
    height: 691px;
    background: var(--burgundy);
    overflow: hidden;
    font-family: "Carlito", "Calibri", sans-serif;
    color: var(--white);
  }
  .card__bands {
    position: absolute;
    inset: 0;
  }
  .hotel-name {
    position: absolute;
    top: 72px;
    right: 52px;
    margin: 0;
    font-family: "Carlito", "Calibri", sans-serif;
    font-weight: 400;
    font-size: 58px;
    line-height: 1;
    color: var(--white);
    white-space: nowrap;
  }
  .contact {
    position: absolute;
    top: 76px;
    left: 68px;
    margin: 0;
    padding: 0;
    list-style: none;
    font-size: 32px;
    line-height: 1.2;
  }
  .contact__item { margin: 0; }
  .contact__item--phone { margin-bottom: 32px; }
  .contact__item--fax { margin-bottom: 32px; }
  .contact__item--cell { margin-bottom: 36px; }
  .contact__item--email { margin-bottom: 36px; }
  .contact__item--address { line-height: 1.45; margin-top: -4px; }
  .contact__label {
    font-style: italic;
    display: inline-block;
    min-width: 84px;
  }
  .contact__item--email .contact__label,
  .contact__item--web .contact__label,
  .contact__item--address .contact__label { min-width: 0; margin-right: 6px; }
  .hotel-sketch {
    position: absolute;
    left: 580px;
    top: 262px;
    width: 620px;
    height: 429px;
  }
  .person-name {
    position: absolute;
    left: 68px;
    top: 598px;
    margin: 0;
    font-size: 34px;
    font-weight: 700;
    font-variant: small-caps;
    letter-spacing: 1px;
    color: var(--burgundy);
  }
</style>
</head>
<body>
  <main class="card">
    <svg class="card__bands" width="1200" height="691" viewBox="0 0 1200 691" aria-hidden="true">
      <path class="band band--top" fill="var(--gold)"
            d="M455,0 C520,150 760,265 1200,320 L1200,430 C760,385 560,250 512,0 Z"/>
      <path class="band band--bottom" fill="var(--gold)"
            d="M0,546 C220,515 480,560 690,691 L0,691 Z"/>
    </svg>

    <h1 class="hotel-name">Mt Brindlewood Hotel</h1>

    <ul class="contact">
      <li class="contact__item contact__item--phone"><span class="contact__label">Ph:</span>00 0000000</li>
      <li class="contact__item contact__item--fax"><span class="contact__label">Fax:</span>00 0000000</li>
      <li class="contact__item contact__item--cell"><span class="contact__label">Cell:</span>00 0000000</li>
      <li class="contact__item contact__item--email"><span class="contact__label">Email:</span>xx@xxxxx.com</li>
      <li class="contact__item contact__item--web"><span class="contact__label">Web:</span>www.xxxxx.com</li>
      <li class="contact__item contact__item--address"><span class="contact__label">Add:</span>xxxxxx xxxxx xxxx<br>xxxxxx 00000</li>
    </ul>

    <svg class="hotel-sketch" viewBox="0 0 620 429" role="img" aria-label="Line drawing of the historic two-storey hotel building with gabled roof, chimneys and verandah">
      <path d="M8,429 L8,130 L120,60 L330,60 L420,8 L520,60 L612,60 L612,429 Z" fill="var(--cream)" stroke="var(--gold)" stroke-width="10" stroke-linejoin="round"/>
    </svg>

    <p class="person-name">Dario Fenwick</p>
  </main>
</body>
</html>
```